Web Design Project for DJ

We need a web design for a DJ. Our client is a freelance DJ who already has a regular gig at a major night club but is looking to expand his exposure. He is located in a major metropolitan area and is looking for further gigs. He is hoping to generate further business via the website, including bookings via the site.

For reference his pagelinker page is here https://www.pagelinker.example/pages/DJ-Vorn/730162948415207

Following face to face discussions with the client today we have made a few small alterations to the brief.  We are hoping to have some images uploaded shortly.

Target Market(s)

Event planners, night club owners, radio stations, younger age groups (16-35)

Industry/Entity Type

Business

Requirements
Must have
• Name is DJVorn, this should obviously feature prominently. His current business card is attached as an example.

Links to Pagelinker and Tunedrift

Cool, modern look, slightly edgy.

Site will be built in Joomla, so a front page and secondary page template is required.
Nice to have
• Blog style layout to front page featuring recent and upcoming gigs.

Secondary pages may include a more expansive blog, a list of upcoming gigs, and a booking form.

Darker colour palettes preferred and use of same/similar fonts to those on the business card are an obvious plus

```html
<!DOCTYPE html>
<html lang="en">
<head>
<meta charset="utf-8">
<title>DJ Vorn – Club &amp; Event DJ</title>
<link href="https://fonts.googleapis.com/css2?family=Arimo:wght@400;700&family=Dancing+Script:wght@700&display=swap" rel="stylesheet">
<style>
:root{
  --page:#3b3b3b;
  --deep:#141414;
  --panel:#1d1d1d;
  --orange:#f07a1c;
  --orange-dark:#c85e0e;
  --orange-light:#ffa24a;
  --green:#5cb84a;
  --text:#444;
  --muted:#888;
  --paper:#ffffff;
  --foot:#ececec;
  --line:#d6d6d6;
}
*{box-sizing:border-box;margin:0;padding:0}
html,body{width:826px;height:1200px;overflow:hidden}
body{background:radial-gradient(ellipse at 50% 30%,#4a4a4a,var(--page) 70%);font-family:"Arimo",Arial,sans-serif;color:var(--text);font-size:10px;position:relative}
.topbar{position:absolute;left:0;top:0;width:826px;height:38px;background:var(--deep);border-bottom:1px solid #2a2a2a}
.site{position:absolute;left:105px;top:0;width:616px;height:1200px}
.tagline{position:absolute;left:0;top:8px;font-family:"Dancing Script",cursive;font-size:16px;color:#e9e9e9}
.social{position:absolute;right:0;top:13px;display:flex;gap:14px;list-style:none}
.social li{display:flex;align-items:center;gap:4px;color:#bbb;font-size:10px}
.social li::before{content:"";width:9px;height:9px;background:#777;border-radius:2px}
.header{position:absolute;left:0;top:38px;width:616px;height:168px;background:linear-gradient(90deg,#1a1a1a,#222 45%,#2c1f2d)}
.hero-photo{position:absolute;right:0;top:0;width:300px;height:168px;background:radial-gradient(circle at 55% 45%,#c7866a,#6e3d4f 40%,#27202e 75%)}
.brand{position:absolute;left:28px;top:62px;display:flex;align-items:center;gap:12px}
.brand-dot{width:22px;height:22px;border-radius:50%;background:var(--orange)}
.brand-name{font-family:"Arimo",sans-serif;font-weight:700;font-size:34px;line-height:1;color:#f2f2f2}
.nav{position:absolute;left:0;top:212px;width:616px;height:32px;background:linear-gradient(#f6902f,var(--orange-dark));border-radius:3px;display:flex;list-style:none;padding-left:10px;align-items:center}
.nav li{font-size:10px;color:#fff;padding:6px 12px}
.nav li.active{background:var(--orange-light);border-radius:2px}
.slider{position:absolute;left:0;top:250px;width:616px;height:170px;background:var(--panel)}
.slide-photo{position:absolute;left:18px;top:12px;width:315px;height:146px;background:linear-gradient(120deg,#1f2b6e,#7a2fa0 50%,#d4527a)}
.slide-text{position:absolute;left:352px;top:14px;width:245px;color:#bbb;font-size:9px;line-height:1.5}
.slide-text h2{font-size:15px;color:var(--orange);font-weight:400;margin-bottom:10px}
.slide-text .more{display:inline-block;margin-top:10px;color:#fff;font-size:9px}
.thumbs{position:absolute;left:0;top:424px;width:616px;height:74px;background:#262626;display:flex;gap:9px;padding:10px 14px}
.thumbs span{flex:1;border:2px solid #555;background:linear-gradient(135deg,#3b2a5c,#8a3e6a)}
.thumbs span:nth-child(2n){background:linear-gradient(135deg,#5c3b1f,#c0722a)}
.thumbs span:nth-child(3n){background:linear-gradient(135deg,#1f3f5c,#3b8ac0)}
.content{position:absolute;left:0;top:504px;width:616px;height:375px;background:var(--paper)}
.welcome{position:absolute;left:12px;top:12px;width:390px}
.bar{background:linear-gradient(#6a6a6a,#4b4b4b);color:#fff;font-size:10px;font-weight:700;padding:6px 8px}
.welcome p{font-size:9px;line-height:1.5;margin-top:7px;color:#555}
.subscribe{position:absolute;left:418px;top:10px;width:186px}
.subscribe h3{font-size:15px;color:#555;font-weight:700;border-bottom:1px solid var(--line);padding-bottom:5px}
.subscribe .field{height:20px;border:1px solid var(--line);margin-top:8px;width:120px;font-size:8px;color:#aaa;padding:5px}
.subscribe .submit{position:absolute;left:128px;top:30px;width:32px;height:18px;background:var(--orange);color:#fff;font-size:7px;text-align:center;line-height:18px;border-radius:2px}
.book-btn{margin-top:14px;height:36px;background:linear-gradient(#6dcc58,var(--green));border-radius:4px;color:#fff;font-weight:700;font-size:13px;text-align:center;line-height:36px}
.features{position:absolute;left:12px;top:190px;width:592px;display:flex;gap:26px}
.feature{flex:1}
.feature h3{font-size:13px;color:#444;font-weight:700;margin-bottom:8px}
.feature .body{display:flex;gap:8px}
.feature .icon{width:58px;height:58px;flex:none;background:linear-gradient(#d5d5d5,#9b9b9b);border-radius:4px}
.feature p{font-size:9px;line-height:1.5;color:#555}
.feature .more{display:inline-block;margin-top:10px;background:var(--orange);color:#fff;font-size:7px;padding:3px 7px;border-radius:2px}
.footer{position:absolute;left:0;top:885px;width:616px;height:255px;background:var(--foot);display:flex;gap:22px;padding:14px 12px}
.footer .col{flex:1}
.footer h4{font-size:8px;font-weight:700;color:#333;text-transform:uppercase;border-bottom:1px solid #cfcfcf;padding-bottom:5px;margin-bottom:7px}
.links{list-style:none}
.links li{font-size:8px;color:#555;padding:4px 0;display:flex;align-items:center;gap:5px}
.updates{list-style:none}
.updates li{display:flex;gap:6px;margin-bottom:7px}
.date{width:26px;height:26px;flex:none;background:#fff;border:1px solid #ccc;font-size:6px;text-align:center;padding-top:4px;color:#666;line-height:1.3}
.updates b{display:block;font-size:8px;color:#333}
.updates small{font-size:6.5px;color:var(--muted)}
.contact p{font-size:8px;line-height:1.5;color:#555;margin-bottom:6px}
.copyright{position:absolute;left:0;top:1146px;width:616px;height:26px;background:var(--deep);color:#aaa;font-size:8px;text-align:center;line-height:26px}
</style>
</head>
<body>
<div class="topbar"></div>
<div class="site">
  <div class="tagline">Your Next Party Is Tonight!</div>
  <ul class="social">
    <li>Pagelinker</li>
    <li>Chirper</li>
    <li>RSS</li>
  </ul>

  <header class="header">
    <div class="hero-photo" role="img" aria-label="Photo of a dancer with headphones and flowing hair under club lights"></div>
    <div class="brand">
      <span class="brand-dot"></span>
      <span class="brand-name">DJ Vorn</span>
    </div>
  </header>

  <ul class="nav">
    <li class="active">Home</li>
    <li>About</li>
    <li>Blog</li>
    <li>Gallery</li>
    <li>Events</li>
    <li>Contacts</li>
    <li>Book A Gig</li>
    <li>Music Mixes</li>
  </ul>

  <section class="slider">
    <div class="slide-photo" role="img" aria-label="Photo of a lit stage with equalizer lights"></div>
    <div class="slide-text">
      <h2>Giusto odio dignissimos</h2>
      <p>At vero eos et accusamus et iusto odio dignissimos ducimus qui blanditiis praesentium voluptatum deleniti atque corrupti quos dolores et quas molestias excepturi sint occaecati cupiditate non provident.</p>
      <span class="more">Read More</span>
    </div>
  </section>

  <div class="thumbs" role="img" aria-label="Row of gig photo thumbnails">
    <span></span><span></span><span></span><span></span><span></span><span></span><span></span>
  </div>

  <main class="content">
    <section class="welcome">
      <div class="bar">Welcome To Night Party With DJ Vorn</div>
      <p>Welcome to the official home of DJ Vorn, resident at one of the city's biggest night clubs. Whether it's a club night, a private party or a festival stage, every set is built for the crowd in front of him, with fresh edits and exclusive mixes every week.</p>
      <p>From deep house warm-ups to peak-time anthems, he reads the room and keeps the floor moving until the lights come up. Event planners, venues and radio stations can check the calendar and book him for your next event below.</p>
    </section>

    <aside class="subscribe">
      <h3>Subscribe Email</h3>
      <div class="field">Name</div>
      <div class="field">Email</div>
      <div class="submit">Submit</div>
      <div class="book-btn">Event Booking</div>
    </aside>

    <div class="features">
      <article class="feature">
        <h3>Event Booking</h3>
        <div class="body">
          <div class="icon" role="img" aria-label="Calendar illustration"></div>
          <p>It is a long established fact that a reader will be distracted by the readable content of a page when looking at its layout.</p>
        </div>
        <span class="more">Read More</span>
      </article>
      <article class="feature">
        <h3>Gallery</h3>
        <div class="body">
          <div class="icon" role="img" aria-label="Camera illustration"></div>
          <p>It is a long established fact that a reader will be distracted by the readable content of a page when looking at its layout.</p>
        </div>
        <span class="more">Read More</span>
      </article>
      <article class="feature">
        <h3>Drinks</h3>
        <div class="body">
          <div class="icon" role="img" aria-label="Cocktail glass illustration"></div>
          <p>It is a long established fact that a reader will be distracted by the readable content of a page when looking at its layout.</p>
        </div>
        <span class="more">Read More</span>
      </article>
    </div>
  </main>

  <footer class="footer">
    <div class="col">
      <h4>Site Navigation</h4>
      <ul class="links">
        <li><svg width="6" height="6" viewBox="0 0 6 6"><path d="M1 0l4 3-4 3z" fill="#f07a1c"/></svg>Home Page</li>
        <li><svg width="6" height="6" viewBox="0 0 6 6"><path d="M1 0l4 3-4 3z" fill="#f07a1c"/></svg>Events</li>
        <li><svg width="6" height="6" viewBox="0 0 6 6"><path d="M1 0l4 3-4 3z" fill="#f07a1c"/></svg>Packages</li>
        <li><svg width="6" height="6" viewBox="0 0 6 6"><path d="M1 0l4 3-4 3z" fill="#f07a1c"/></svg>About Us</li>
        <li><svg width="6" height="6" viewBox="0 0 6 6"><path d="M1 0l4 3-4 3z" fill="#f07a1c"/></svg>Contact Us</li>
      </ul>
    </div>
    <div class="col">
      <h4>New Updates</h4>
      <ul class="updates">
        <li><div class="date">Jun<br>12</div><div><b>New Mix Out This Week</b><small>Posted in news and gigs</small></div></li>
        <li><div class="date">Jun<br>15</div><div><b>Rooftop Party Saturday</b><small>Posted in news and gigs</small></div></li>
        <li><div class="date">Jun<br>19</div><div><b>Live Set On Radio</b><small>Posted in news and gigs</small></div></li>
        <li><div class="date">Jun<br>22</div><div><b>Tickets For Friday Night</b><small>Posted in news and gigs</small></div></li>
      </ul>
    </div>
    <div class="col contact">
      <h4>Contact</h4>
      <p>Got an event coming up? Send the date, venue and expected crowd size and we will reply within two working days with availability.</p>
      <p>Vorn Bookings Ltd<br>1234 Harbour Street, Suite 40<br>Phone: 555 0142 880<br>Email: book@djvorn.example</p>
    </div>
  </footer>

  <div class="copyright">Copyright © 2012 DJ Vorn</div>
</div>
</body>
</html>
```